Casa Vero Inspections Business Card

I need a business card for my new company. The company is going to provide home inspections. The name of the company is Casa Vero Inspections. I am not sure if I want a single sided card or a double. I have a logo already that I want to incorporate into the card design. I was wondering if I should incorporate a catch phrase on my card or not. If I did the phrase would be "The Intelligent Choice for Home Inspections" but i am unsure how or if to use it on a card. The following information needs to be on the card.
Home Inspection
My Name: Marcus T. Wolford Phone Number: 555-301-7762 Email: mwolford@casaveroinspections.com Website: www.casaveroinspections.com NY HI License # 27300519462

```html
<!DOCTYPE html>
<html lang="en">
<head>
<meta charset="utf-8">
<title>Casa Vero Inspections Business Card</title>
<link href="https://fonts.googleapis.com/css2?family=Montserrat:wght@600;700&family=Roboto:wght@400&display=swap" rel="stylesheet">
<style>
  :root {
    --page-bg: #e9ecef;
    --card-white: #ffffff;
    --brand-blue: #0a6bb0;
    --brand-blue-deep: #075a96;
    --accent-blue: #3aa3e3;
    --rule-blue: #7cc3ee;
    --text-dark: #333a40;
    --text-grey: #6b7178;
  }
  * { box-sizing: border-box; margin: 0; padding: 0; }
  html, body {
    width: 1200px; height: 900px; overflow: hidden;
    background: var(--page-bg);
  }
  .sheet {
    width: 1200px; height: 900px;
    display: flex; flex-direction: column;
    align-items: center; justify-content: center; gap: 40px;
  }
  .card {
    width: 665px; height: 380px;
    border-radius: 14px;
    position: relative;
    box-shadow: 0 6px 18px rgba(0,0,0,0.12);
  }
  .card-front { background: var(--card-white); }
  .card-back {
    background: var(--brand-blue);
    display: flex; align-items: center; justify-content: center;
  }

  .identity { position: absolute; left: 48px; top: 46px; }
  .person-name {
    font-family: 'Montserrat', sans-serif; font-weight: 700;
    font-size: 30px; letter-spacing: -0.5px;
    color: var(--brand-blue); text-transform: uppercase;
  }
  .person-name .initial { color: var(--accent-blue); }
  .person-role {
    font-family: 'Roboto', sans-serif; font-size: 15px;
    color: var(--text-grey); margin-top: 2px;
  }
  .divider {
    position: absolute; left: 48px; right: 40px; top: 138px;
    height: 1px; background: var(--rule-blue);
  }
  .contacts {
    position: absolute; left: 48px; top: 160px;
    list-style: none;
    font-family: 'Roboto', sans-serif; font-size: 15px; color: var(--text-dark);
  }
  .contacts li { display: flex; align-items: center; gap: 8px; line-height: 25px; }
  .contacts svg { width: 13px; height: 13px; flex: none; }
  .contacts .web { color: var(--brand-blue); }
  .license {
    position: absolute; left: 48px; top: 240px;
    font-family: 'Roboto', sans-serif; font-size: 15px; color: var(--text-dark);
    line-height: 25px;
  }

  .brand-front {
    position: absolute; right: 44px; bottom: 46px;
    display: flex; align-items: center; gap: 10px;
  }
  .brand-name {
    font-family: 'Montserrat', sans-serif; font-weight: 700;
    text-transform: uppercase; letter-spacing: 0.5px;
    white-space: nowrap;
  }
  .brand-front .brand-name { font-size: 22px; color: var(--brand-blue); }
  .brand-mark { width: 13px; height: 13px; background: var(--accent-blue); }
  .card-back .brand-name { font-size: 40px; color: var(--brand-blue-deep); }
</style>
</head>
<body>
<main class="sheet">
  <section class="card card-front" aria-label="Card front">
    <div class="identity">
      <h1 class="person-name">Marcus <span class="initial">T.</span> Wolford</h1>
      <p class="person-role">Inspector</p>
    </div>
    <div class="divider"></div>
    <ul class="contacts">
      <li>
        <svg viewBox="0 0 16 16" aria-hidden="true"><path fill="#0a6bb0" d="M3.5 1.5l2.5 0 1 3.5-1.6 1.2a9 9 0 0 0 4.4 4.4L11 9l3.5 1v2.5c0 1-.8 2-2 2C6.5 14.5 1.5 9.5 1.5 3.5c0-1.2 1-2 2-2z"/></svg>
        555-301-7762
      </li>
      <li>
        <svg viewBox="0 0 16 16" aria-hidden="true"><rect x="1" y="3" width="14" height="10" rx="1.5" fill="none" stroke="#0a6bb0" stroke-width="1.6"/><path d="M1.5 4l6.5 5 6.5-5" fill="none" stroke="#0a6bb0" stroke-width="1.6"/></svg>
        mwolford@casaveroinspections.com
      </li>
      <li>
        <svg viewBox="0 0 16 16" aria-hidden="true"><circle cx="8" cy="8" r="7" fill="#0a6bb0"/><path d="M1 8h14M8 1c-3 3.5-3 10.5 0 14M8 1c3 3.5 3 10.5 0 14" fill="none" stroke="#fff" stroke-width="1"/></svg>
        <span class="web">www.casaveroinspections.com</span>
      </li>
    </ul>
    <p class="license">NY HI License # 27300519462</p>
    <div class="brand-front">
      <span class="brand-mark" aria-hidden="true"></span>
      <span class="brand-name">Casa Vero Inspections</span>
    </div>
  </section>

  <section class="card card-back" aria-label="Card back">
    <span class="brand-name">Casa Vero Inspections</span>
  </section>
</main>
</body>
</html>
```